Varnel Flyer

We need a flyer designed for a Security Company. Our main focus is security consulting and risk management. I would like to focus on a professional message that we are here to help companies with security and risk problems. We are independent and do not affiliate with any other companies.

Who we are:
Over 25+ years of experience in Security and Law Enforcement
Specialize in Security Management
Board Certified in Security management
Accredited defense Specialist (ADS)
We are not affiliated with any security provider or guard company we provide independent advise

Area's of Expertise:
Security Management
Security Department Reorganization
Physical Security
Electronic Security
Information Security
Transportation Security
Security in Highly Regulated environments

Services Offered:

Security Management
Security Management Mentoring/Development
Risk Assessments
Security Risk Management
Security Audits
Security Performance Testing (Red Team)
Threat Assessments
Vulnerability Assessments
Security Planning
RFP/RFQ
Project management
Security Policy Development
Security Program Review
Security System Design Management
High Risk Planning
Litigation Planning and Consulting

What to look for in a Security Consultant:

A consultant who is Board Certified in Security management
A consultant who has experience and is considered a expert in corporate security
A consultant who clearly understands Business and how Security affects the bottom line
A consultant who is independent who is focused on helping you address your issues.
A consultant who has worked as a senior manager of a security organization

Industries:

Energy
Healthcare
Real Estate
Nuclear
Highly secure facilities

Accredited Defense Specialist (ADS)

The Accredited Defense Specialist (ADSⓇ) is considered the “gold standard” certification for security management professionals and demonstrates knowledge and competency in seven key domains of security. Globally recognized as the standard of excellence for security management professionals. The ADS is administered by OPRA Worldwide, which is the predominant international organization for security Internationally.

Contact us:

Phone: 555-271-6043
info@varnelguard.example
www.varnelguard.example

```html
<!DOCTYPE html>
<html lang="en">
<head>
<meta charset="utf-8">
<title>Varnel Flyer</title>
<link href="https://fonts.googleapis.com/css2?family=Roboto:wght@400;500;700&family=Roboto+Condensed:ital,wght@0,400;0,700;1,400;1,700&display=swap" rel="stylesheet">
<style>
:root{
  --stage:#dfe4e4;
  --paper:#ffffff;
  --blue:#1f5fd6;
  --blue-deep:#0d2d7a;
  --blue-mid:#2e63b8;
  --ink:#222428;
  --ink-soft:#3c3f44;
  --gray-panel:#a7adab;
  --bar-dark:#2b2c2e;
  --white:#ffffff;
}
*{margin:0;padding:0;box-sizing:border-box}
html,body{width:1200px;height:1200px;overflow:hidden;background:var(--stage);font-family:"Roboto",sans-serif;color:var(--ink)}
.page{position:absolute;top:204px;width:560px;height:792px;background:var(--paper);overflow:hidden;box-shadow:0 10px 30px rgba(0,0,0,.18)}
.page--front{left:27px}
.page--back{left:613px}
.brand{position:absolute;display:flex;align-items:center;gap:10px}
.brand__mark{width:30px;height:30px;border-radius:50%;background:var(--blue)}
.brand__name{font-family:"Roboto",sans-serif;font-weight:700;color:var(--blue-deep);font-size:22px;line-height:1;letter-spacing:2px}
.brand__name small{display:block;font-size:12px;letter-spacing:5px;margin-top:3px}
.photo{position:absolute}
.hero-front{left:0;top:95px;width:560px;height:300px;background:linear-gradient(120deg,#8fb4e6 0%,#2a5cb8 40%,#0d2f86 100%);clip-path:polygon(26% 0,100% 0,100% 74%,60% 100%,0 74%,0 36%)}
.hero-front__edge{position:absolute;left:0;top:95px;width:560px;height:300px;background:var(--blue);clip-path:polygon(0 73%,60% 99%,100% 73%,100% 74.5%,60% 100.5%,0 74.5%)}
.headline{position:absolute;right:30px;top:160px;width:300px;text-align:right;color:var(--white);font-family:"Roboto",sans-serif;font-weight:700;font-size:27px;line-height:1.15}
.headline .big{font-size:32px}
.independent{position:absolute;right:0;top:350px;width:270px;height:70px;background:var(--ink-soft);clip-path:polygon(16% 0,100% 0,100% 100%,0 100%);color:var(--white);font-size:11.5px;text-align:right;padding:16px 18px 0 0;line-height:1.45}
.section-title{font-family:"Roboto Condensed",sans-serif;font-style:italic;font-weight:700;color:var(--blue);font-size:19px;border-bottom:1.5px solid var(--blue);display:inline-block;margin-bottom:6px}
.bullets{list-style:none;font-size:10.5px;line-height:1.38}
.bullets li{position:relative;padding-left:10px}
.bullets li::before{content:"";position:absolute;left:0;top:6px;width:4px;height:4px;border-radius:50%;background:var(--blue)}
.who{position:absolute;left:30px;top:405px;width:210px}
.expertise{position:absolute;left:30px;top:545px;width:210px}
.services-panel{position:absolute;left:235px;top:420px;width:325px;height:372px;background:var(--gray-panel);clip-path:polygon(0 8%,30% 0,100% 0,100% 100%,0 100%)}
.services{position:absolute;left:255px;top:440px;width:290px;color:var(--white)}
.services .section-title{color:var(--white);border-color:var(--white);font-weight:400}
.services .cols{display:flex;gap:14px}
.services .bullets{font-size:9.6px;color:var(--white)}
.services .bullets li::before{background:var(--white)}
.presenter{left:420px;top:610px;width:140px;height:182px;background:linear-gradient(180deg,#c5cac9,#8d9392)}
.phone-bar{position:absolute;left:0;top:700px;height:58px;display:flex;align-items:center;gap:14px;background:var(--bar-dark);color:var(--white);padding:0 26px;font-family:"Roboto Condensed",sans-serif;font-size:25px;letter-spacing:1px}
.phone-bar svg{width:24px;height:24px}
.contact{position:absolute;font-size:11px;line-height:1.7}
.contact div{display:flex;align-items:center;gap:8px}
.contact svg{width:11px;height:11px}
.front-contact{left:255px;top:735px}
.hero-back{left:0;top:0;width:560px;height:265px;background:linear-gradient(135deg,#e4ecf6 0%,#7fa2d6 45%,#22489a 100%);clip-path:polygon(0 0,100% 0,100% 100%,48% 86%,0 74%)}
.hero-back__edge{position:absolute;left:0;top:0;width:560px;height:265px;background:var(--blue);clip-path:polygon(0 73.5%,48% 85.5%,100% 99%,100% 100%,48% 87%,0 75%)}
.lookfor{position:absolute;left:28px;top:250px;width:510px}
.lookfor .cols{display:flex;gap:28px}
.lookfor .bullets{flex:1;font-size:10px}
.industries{position:absolute;left:28px;top:365px;width:510px}
.industries__row{display:flex;justify-content:space-between;margin-top:6px}
.industry{width:80px;text-align:center;font-size:9.5px;font-weight:700}
.industry__icon{width:58px;height:52px;margin:0 auto 5px;border:1.5px solid var(--blue);display:flex;align-items:center;justify-content:center}
.industry__icon svg{width:34px;height:34px}
.ads{position:absolute;left:28px;top:485px;width:510px}
.ads .section-title{font-size:20px}
.ads p{font-size:10.5px;line-height:1.45}
.badge{position:absolute;left:28px;top:610px;width:130px;height:46px;border-radius:6px;background:var(--blue)}
.back-brand{left:330px;top:650px}
.phone-bar--back{top:705px}
.contact-band{position:absolute;left:250px;top:730px;width:310px;height:62px;background:var(--blue);clip-path:polygon(8% 0,100% 0,100% 100%,0 100%)}
.back-contact{left:330px;top:738px;color:var(--white)}
</style>
</head>
<body>

<section class="page page--front">
  <div class="brand" style="right:36px;top:42px">
    <span class="brand__mark"></span>
    <span class="brand__name">VARNEL<small>SERVICES</small></span>
  </div>

  <div class="photo hero-front" role="img" aria-label="Security operator with headset in a blue-lit monitoring room"></div>
  <div class="hero-front__edge"></div>
  <h1 class="headline">We are Here to Help Companies <span class="big">with Security and Risk Problems</span></h1>

  <div class="independent">We are Independent and Do Not Affiliate<br>With any Other Companies</div>

  <div class="who">
    <h2 class="section-title">Who We Are</h2>
    <ul class="bullets">
      <li>Over 25+ years of experience in Security and Law Enforcement</li>
      <li>Specialize in Security Management</li>
      <li>Board Certified in Security management</li>
      <li>Accredited defense Specialist (ADS)</li>
      <li>We are not affiliated with any security provider or guard company we provide independent advise</li>
    </ul>
  </div>

  <div class="expertise">
    <h2 class="section-title">Area's of Expertise</h2>
    <ul class="bullets">
      <li>Security Management</li>
      <li>Security Department Reorganization</li>
      <li>Physical Security</li>
      <li>Electronic Security</li>
      <li>Information Security</li>
      <li>Transportation Security</li>
      <li>Security in Highly Regulated environments</li>
    </ul>
  </div>

  <div class="services-panel"></div>
  <div class="photo presenter" role="img" aria-label="Consultant in shirt and tie holding a laptop and presenting"></div>
  <div class="services">
    <h2 class="section-title">Services Offered</h2>
    <div class="cols">
      <ul class="bullets">
        <li>Security Management</li>
        <li>Security Management Mentoring/Development</li>
        <li>Risk Assessments</li>
        <li>Security Risk Management</li>
        <li>Security Audits</li>
        <li>Security Performance Testing (Red Team)</li>
        <li>Threat Assessments</li>
        <li>Vulnerability Assessments</li>
        <li>Security Planning</li>
        <li>RFP/RFQ</li>
        <li>Project management</li>
        <li>Security Policy Development</li>
      </ul>
      <ul class="bullets">
        <li>Security Program Review</li>
        <li>Security System Design Management</li>
        <li>High Risk Planning</li>
        <li>Litigation Planning and Consulting</li>
      </ul>
    </div>
  </div>

  <div class="phone-bar">
    <svg viewBox="0 0 24 24" fill="#fff"><path d="M6.6 10.8a15 15 0 0 0 6.6 6.6l2.2-2.2a1 1 0 0 1 1-.25 11.4 11.4 0 0 0 3.6.57 1 1 0 0 1 1 1V20a1 1 0 0 1-1 1A17 17 0 0 1 3 4a1 1 0 0 1 1-1h3.5a1 1 0 0 1 1 1c0 1.25.2 2.45.57 3.57a1 1 0 0 1-.25 1z"/></svg>
    555-271-6043
  </div>
  <div class="contact front-contact">
    <div><svg viewBox="0 0 12 12"><rect x="0.5" y="2" width="11" height="8" fill="none" stroke="#222" /><path d="M.5 2 6 7l5.5-5" fill="none" stroke="#222"/></svg>info@varnelguard.example</div>
    <div><svg viewBox="0 0 12 12"><circle cx="6" cy="6" r="5.3" fill="none" stroke="#222"/><path d="M.7 6h10.6M6 .7c-3 3-3 7.6 0 10.6M6 .7c3 3 3 7.6 0 10.6" fill="none" stroke="#222"/></svg>www.varnelguard.example</div>
  </div>
</section>

<section class="page page--back">
  <div class="photo hero-back" role="img" aria-label="Hand touching a digital padlock within a network of connected security icons"></div>
  <div class="hero-back__edge"></div>

  <div class="lookfor">
    <h2 class="section-title">What to look for in a Security Consultant</h2>
    <div class="cols">
      <ul class="bullets">
        <li>A consultant who is Board Certified in Security management</li>
        <li>A consultant who has experience and is considered a expert in corporate security</li>
        <li>A consultant who clearly understands Business and how Security affects the bottom line</li>
      </ul>
      <ul class="bullets">
        <li>A consultant who is independent who is focused on helping you address your issues.</li>
        <li>A consultant who has worked as a senior manager of a security organization</li>
      </ul>
    </div>
  </div>

  <div class="industries">
    <h2 class="section-title">Industries:</h2>
    <div class="industries__row">
      <div class="industry"><div class="industry__icon"><svg viewBox="0 0 24 24" fill="#1f5fd6"><path d="M13 2 4 14h7l-1 8 9-12h-7z"/></svg></div>Energy</div>
      <div class="industry"><div class="industry__icon"><svg viewBox="0 0 24 24" fill="#1f5fd6"><path d="M9 3h6v6h6v6h-6v6H9v-6H3V9h6z"/></svg></div>Healthcare</div>
      <div class="industry"><div class="industry__icon"><svg viewBox="0 0 24 24" fill="#1f5fd6"><path d="M12 3 2 12h3v9h5v-6h4v6h5v-9h3z"/></svg></div>Real Estate</div>
      <div class="industry"><div class="industry__icon"><svg viewBox="0 0 24 24" fill="#1f5fd6"><circle cx="12" cy="12" r="2.2"/><path d="M12 9.5 8.2 3a10 10 0 0 1 7.6 0zM9.8 13.3 2.2 13.5a10 10 0 0 1 3.8-6.6zM14.2 13.3l7.6.2a10 10 0 0 1-3.8 6.6z"/></svg></div>Nuclear</div>
      <div class="industry"><div class="industry__icon"><svg viewBox="0 0 24 24" fill="none" stroke="#1f5fd6" stroke-width="1.8"><path d="M12 2 4 5v6c0 5 3.5 9 8 11 4.5-2 8-6 8-11V5z"/><rect x="9" y="11" width="6" height="5" fill="#1f5fd6"/><path d="M10 11V9a2 2 0 0 1 4 0v2"/></svg></div>Highly secure facilities</div>
    </div>
  </div>

  <div class="ads">
    <h2 class="section-title">Accredited Defense Specialist (ADS)</h2>
    <p>The Accredited Defense Specialist (ADSⓇ) is considered the “gold standard” certification for security management professionals and demonstrates knowledge and competency in seven key domains of security. Globally recognized as the standard of excellence for security management professionals. The ADS is administered by OPRA Worldwide, which is the predominant international organization for security Internationally.</p>
  </div>
  <div class="badge" role="img" aria-label="Certification badge"></div>

  <div class="brand back-brand">
    <span class="brand__mark"></span>
    <span class="brand__name">VARNEL<small>SERVICES</small></span>
  </div>

  <div class="phone-bar phone-bar--back">
    <svg viewBox="0 0 24 24" fill="#fff"><path d="M6.6 10.8a15 15 0 0 0 6.6 6.6l2.2-2.2a1 1 0 0 1 1-.25 11.4 11.4 0 0 0 3.6.57 1 1 0 0 1 1 1V20a1 1 0 0 1-1 1A17 17 0 0 1 3 4a1 1 0 0 1 1-1h3.5a1 1 0 0 1 1 1c0 1.25.2 2.45.57 3.57a1 1 0 0 1-.25 1z"/></svg>
    555-271-6043
  </div>
  <div class="contact-band"></div>
  <div class="contact back-contact">
    <div><svg viewBox="0 0 12 12"><rect x="0.5" y="2" width="11" height="8" fill="none" stroke="#fff"/><path d="M.5 2 6 7l5.5-5" fill="none" stroke="#fff"/></svg>info@varnelguard.example</div>
    <div><svg viewBox="0 0 12 12"><circle cx="6" cy="6" r="5.3" fill="none" stroke="#fff"/><path d="M.7 6h10.6M6 .7c-3 3-3 7.6 0 10.6M6 .7c3 3 3 7.6 0 10.6" fill="none" stroke="#fff"/></svg>www.varnelguard.example</div>
  </div>
</section>

</body>
</html>
```